New HR Software Platform needs Process Flow Graphic.

larkvalehiring.com is launching a new HR Applicant Tracking Platform to streamline a company's applicant flow and reduce spend. We would like a graphic design be created for "TalonStaff" so that the design may be used on our website and marketing pdf and in print (in brochures and so forth). The appropriate file formats .png, .ai, etc should be made available by the winning designer for our exclusive use to expand and modify as we deem necessary. The graphic design should feature a similar color green as used on brixwellmail.com, as well as, coordinating with colors as used on larkvalehiring.com.

Our product is targeted towards companies who do not already have an Applicant Tracking System, even though it is possible existing users may want to switch to our system. TalonStaff allows a company to accept all of its employment applications online with several perks. _We want to highlight the advantages of leveraging Social Media in recruiting_ since TalonStaff makes it easy to advertise jobs as such. Additionally, we believe that a company will significantly reduce spend on job advertisements after adopting our platform for their application process.

We have attached a crude sketch using the outline of our company's trademark "bulb" logo as a basis of the graphical flow chart. The process outlines all the automation of our system before a hiring manager ever interviews an applicant, saving countless labor hours. We would like to preserve the bulb's shape and angle of tilt as can be seen on our website. We believe this platform represents the future of Human resources automation and are excited to start our branding of the product here.

Target Market(s)

Companies with 50 or more employees

Font styles to use
Sans Serif

Colors
add136
f04b51

Requirements
Must have
• Please use our trademark "bulb" using the terminology in the handwritten graphic supplied.
Nice to have
• I would like to see a design that illustrates our process easily. Simple is the key

```html
<!DOCTYPE html>
<html lang="en">
<head>
<meta charset="utf-8">
<title>TalonStaff – Applicant Tracking Process Flow</title>
<link href="https://fonts.googleapis.com/css2?family=Arimo:wght@400;700&display=swap" rel="stylesheet">
<style>
  :root {
    --bg: #58595b;
    --brand-red: #f04b51;
    --brand-green: #7dc243;
    --accent-green: #add136;
    --white: #ffffff;
    --purple-light: #5e3d8f;
    --purple-dark: #2f2868;
    --blue-light: #2a73b8;
    --blue-dark: #2c3a8c;
    --green-light: #22a04c;
    --green-dark: #0c6330;
    --marker: #8cc63f;
    --social: #4aa3df;
  }
  html, body { margin: 0; padding: 0; overflow: hidden; background: var(--bg); }
  .canvas {
    position: relative;
    width: 1200px;
    height: 1000px;
    background: var(--bg);
    font-family: "Arimo", Arial, sans-serif;
    overflow: hidden;
  }
  .features-title {
    position: absolute; left: 168px; top: 28px; margin: 0;
    font-size: 64px; font-weight: 400; color: var(--brand-red); letter-spacing: 1px;
  }
  .feature-list { position: absolute; left: 0; top: 0; margin: 0; padding: 0; list-style: none; z-index: 2; }
  .feature {
    position: absolute; left: 125px; white-space: nowrap;
    font-size: 23px; line-height: 32px; color: var(--brand-green);
  }
  .feature-arrow { position: absolute; left: 20px; }
  .flow { position: absolute; left: 0; top: 0; }
  .step-label { font-family: "Arimo", Arial, sans-serif; fill: var(--white); font-weight: 400; }
  .step-num { font-family: "Arimo", Arial, sans-serif; fill: var(--brand-red); font-weight: 700; }
  .product-name {
    position: absolute; left: 650px; top: 305px; width: 400px; margin: 0; text-align: center;
    font-size: 54px; font-weight: 700; color: var(--brand-green);
    text-shadow: 2px 3px 4px rgba(0,0,0,.45);
  }
  .product-tag {
    position: absolute; left: 650px; top: 382px; width: 400px; margin: 0; text-align: center;
    font-size: 19px; font-weight: 700; color: var(--brand-red);
  }
  .network-tags {
    font-family: "Arimo", Arial, sans-serif; font-size: 8px; fill: var(--white); font-weight: 700;
  }
  .seekers-note {
    position: absolute; left: 870px; top: 878px; width: 330px; margin: 0; text-align: center;
    font-size: 15px; line-height: 19px; color: var(--brand-red);
  }
</style>
</head>
<body>
<div class="canvas">

  <h1 class="features-title">Features</h1>

  <svg class="feature-arrow" width="100" height="560" viewBox="0 0 100 560" style="top:0">
    <defs>
      <linearGradient id="arrPurple"><stop offset="0" stop-color="#3a2a70"/><stop offset="1" stop-color="#5e3d8f"/></linearGradient>
      <linearGradient id="arrBlue"><stop offset="0" stop-color="#2c3a8c"/><stop offset="1" stop-color="#2a73b8"/></linearGradient>
      <linearGradient id="arrGreen"><stop offset="0" stop-color="#0c6330"/><stop offset="1" stop-color="#22a04c"/></linearGradient>
      <linearGradient id="arrYellow"><stop offset="0" stop-color="#f7a51c"/><stop offset="1" stop-color="#f9d423"/></linearGradient>
      <linearGradient id="arrOrange"><stop offset="0" stop-color="#e8452c"/><stop offset="1" stop-color="#f7931e"/></linearGradient>
      <linearGradient id="arrRed"><stop offset="0" stop-color="#c1272d"/><stop offset="1" stop-color="#e8352c"/></linearGradient>
      <g id="chevArrow">
        <path d="M10 0 L22 0 L32 18 L22 36 L10 36 L20 18 Z" opacity=".55"/>
        <path d="M24 0 L36 0 L46 18 L36 36 L24 36 L34 18 Z" opacity=".75"/>
        <path d="M38 0 L70 0 L88 18 L70 36 L38 36 L48 18 Z"/>
      </g>
    </defs>
    <use href="#chevArrow" x="0" y="104" fill="url(#arrPurple)"/>
    <use href="#chevArrow" x="0" y="172" fill="url(#arrBlue)"/>
    <use href="#chevArrow" x="0" y="240" fill="url(#arrGreen)"/>
    <use href="#chevArrow" x="0" y="300" fill="url(#arrYellow)"/>
    <use href="#chevArrow" x="0" y="373" fill="url(#arrOrange)"/>
    <use href="#chevArrow" x="0" y="462" fill="url(#arrRed)"/>
  </svg>

  <ul class="feature-list">
    <li class="feature" style="top:102px">Improve image and visibility to applicants</li>
    <li class="feature" style="top:177px">Effortless applicant screening</li>
    <li class="feature" style="top:243px">Steady applicant flow</li>
    <li class="feature" style="top:304px">Free up time for more important<br>tasks</li>
    <li class="feature" style="top:376px">EEOC/ OFCCP reporting<br>and compliance</li>
    <li class="feature" style="top:462px">Reduce dependence<br>on expensive job posting<br>advertisements</li>
  </ul>

  <svg class="flow" width="1200" height="1000" viewBox="0 0 1200 1000">
    <defs>
      <linearGradient id="gPurple" x1="0" y1="1" x2="1" y2="0">
        <stop offset="0" stop-color="var(--purple-light)"/><stop offset="1" stop-color="var(--purple-dark)"/>
      </linearGradient>
      <linearGradient id="gBlue" x1="0" y1="0" x2="1" y2="1">
        <stop offset="0" stop-color="var(--blue-light)"/><stop offset="1" stop-color="var(--blue-dark)"/>
      </linearGradient>
      <linearGradient id="gGreen" x1="1" y1="0" x2="0" y2="1">
        <stop offset="0" stop-color="var(--green-light)"/><stop offset="1" stop-color="var(--green-dark)"/>
      </linearGradient>
      <linearGradient id="gAuthorize" x1="0" y1="0" x2="1" y2="0">
        <stop offset="0" stop-color="#f7941d"/><stop offset="1" stop-color="#f9e11e"/>
      </linearGradient>
      <linearGradient id="gAssess" x1="0" y1="0" x2="1" y2="0">
        <stop offset="0" stop-color="#f47b20"/><stop offset="1" stop-color="#e23a2a"/>
      </linearGradient>
      <linearGradient id="gConnect" x1="0" y1="0" x2="1" y2="0">
        <stop offset="0" stop-color="#d1262c"/><stop offset="1" stop-color="#b51f2a"/>
      </linearGradient>
    </defs>

    <path class="band band-advertise" fill="url(#gPurple)"
      d="M520 640 C465 600 470 520 510 430 C555 320 620 200 720 140 C780 105 840 95 885 95
         C815 120 740 170 690 240 C640 310 612 380 595 450 C580 520 580 580 600 625 Z"/>
    <path class="band band-network" fill="url(#gBlue)"
      d="M815 162 C880 128 975 125 1040 175 C1100 225 1115 320 1090 390 C1082 415 1075 430 1070 440
         C1072 390 1065 330 1040 280 C1005 215 920 170 815 162 Z"/>
    <path class="band band-screen" fill="url(#gGreen)"
      d="M1105 272 C1150 350 1150 470 1110 545 C1060 640 930 690 800 710
         C720 722 650 760 612 835 C600 770 630 700 700 672
         C820 625 960 610 1030 545 C1090 485 1112 380 1105 272 Z"/>

    <g class="marker" fill="var(--marker)" opacity=".9">
      <path d="M478 575 L545 560 L570 600 L505 615 Z"/>
      <path d="M540 345 L615 355 L605 380 L535 372 Z"/>
      <path d="M783 96 L812 92 L820 118 L790 122 Z"/>
      <path d="M1050 322 L1092 308 L1098 336 L1058 348 Z"/>
      <path d="M1020 560 L1062 538 L1090 590 L1045 608 Z"/>
      <path d="M788 628 L820 625 L842 700 L808 712 Z"/>
      <path d="M612 770 L640 762 L650 800 L620 808 Z"/>
    </g>
    <g class="chevrons" fill="none" stroke="#3fb45a" stroke-width="7" opacity=".7">
      <path d="M545 400 L575 385 L605 400"/>
      <path d="M545 420 L575 405 L605 420"/>
      <path d="M545 440 L575 425 L605 440"/>
      <path d="M870 640 L850 655 L870 672"/>
      <path d="M855 640 L835 655 L855 672"/>
      <path d="M840 642 L820 658 L840 675"/>
      <path d="M1050 530 L1070 555 L1045 575"/>
      <path d="M1035 540 L1055 565 L1030 585"/>
    </g>

    <text class="step-num" font-size="26" transform="translate(528,592) rotate(-12)">1</text>
    <text class="step-num" font-size="24" x="574" y="352">2</text>
    <text class="step-num" font-size="13" transform="translate(806,110) rotate(80)">3</text>
    <text class="step-num" font-size="14" transform="translate(1075,340) rotate(-10)">4</text>
    <text class="step-num" font-size="26" transform="translate(1038,600) rotate(-20)">5</text>
    <text class="step-num" font-size="26" transform="translate(788,672) rotate(95)">6</text>
    <text class="step-num" font-size="12" x="620" y="800">7</text>

    <text class="step-label" font-size="46" transform="translate(548,550) rotate(-70)">POST</text>
    <text class="step-label" font-size="46" transform="translate(590,310) rotate(-58)">ADVERTISE</text>
    <text class="step-label" font-size="38" transform="translate(928,168) rotate(45)">NETWORK</text>
    <text class="step-label" font-size="34" transform="translate(1092,378) rotate(82)">RECEIVE</text>
    <text class="step-label" font-size="34" transform="translate(890,672) rotate(-17)">SCREEN</text>
    <text class="step-label" font-size="42" transform="translate(666,735) rotate(-14)">SIGN</text>

    <g class="network-tags" transform="translate(988,178) rotate(45)">
      <rect x="0" y="-7" width="7" height="7" rx="1" fill="var(--social)"/>
      <text x="10" y="0">Chirply</text>
      <rect x="46" y="-7" width="7" height="7" rx="1" fill="var(--social)"/>
      <text x="56" y="0">Proline</text>
      <rect x="92" y="-7" width="7" height="7" rx="1" fill="var(--social)"/>
      <text x="102" y="0">Facewall</text>
    </g>

    <g transform="translate(505,745) rotate(42)">
      <rect x="-118" y="-28" width="236" height="56" rx="28" fill="url(#gAuthorize)"/>
      <text class="step-label" font-size="28" x="-82" y="10">AUTHORIZE</text>
    </g>
    <g transform="translate(468,792) rotate(44)">
      <rect x="-100" y="-27" width="200" height="54" rx="27" fill="url(#gAssess)"/>
      <text class="step-label" font-size="30" x="-66" y="11">ASSESS</text>
    </g>
    <g transform="translate(428,855) rotate(38)">
      <rect x="-62" y="-24" width="124" height="48" rx="24" fill="url(#gConnect)"/>
      <text class="step-label" font-size="18" x="-45" y="7">CONNECT</text>
    </g>

    <text class="step-num" font-size="13" transform="translate(430,694) rotate(42)">8</text>
    <text class="step-num" font-size="13" x="506" y="886">9</text>

    <path d="M978 700 L978 712 L970 712 L984 728 L998 712 L990 712 L990 700 Z" fill="var(--brand-red)"/>
    <g fill="none" stroke="var(--brand-red)">
      <circle cx="1012" cy="795" r="58" stroke-width="3"/>
      <circle cx="1012" cy="795" r="46" stroke-width="3"/>
      <line x1="966" y1="797" x2="1058" y2="797" stroke-width="3"/>
    </g>
    <text x="1012" y="786" text-anchor="middle" font-family="Arimo, Arial, sans-serif" font-size="18" fill="var(--brand-red)">Job</text>
    <text x="1012" y="822" text-anchor="middle" font-family="Arimo, Arial, sans-serif" font-size="11" fill="var(--brand-red)">SEEKEERS</text>
  </svg>

  <p class="product-name">TalonStaff</p>
  <p class="product-tag">Applicant traking platform</p>
  <p class="seekers-note">Candidates not meeting job requirements<br>are omitted, notified and stored</p>

</div>
</body>
</html>
```